Electrician Business Card/ company logo/small business

New Business Cards and logo needed that will catch peoples eye and say we went that extra step. Attached is a design possibly to be incorporated, if u have your own great, lets see it!... This will be a small local business. thank you for all you do!
Corvane Electric
Wren Osloby Owner
Journeyman Electrician
phone 1.360.428.6037
email: KLXCorvaneElectric@mailvex.net
call for free estimate!

Target Market(s)

support small local business

Industry/Entity Type

Electrical,

Contact Information for Business Card

name, title,company/ logo, phone, email, free estimate

Font styles to use
Other font styles liked:
• easy to read

Colors

Designer to choose colors to be used in the design.

Requirements
Must have
• eye catching everything! logo and corvane electric listed on business card/logo, incorp logo in the background of card
Nice to have
• lightening bolts in eyes or around the triangle? vertical, modern, any design that would be unique and stand out
Should not have
• pinks, reds, yellows,brown

```html
<!DOCTYPE html>
<html lang="en">
<head>
<meta charset="utf-8">
<title>Corvane Electric – Business Card</title>
<link rel="stylesheet" href="https://fonts.googleapis.com/css2?family=Michroma&family=Arimo:wght@400&display=swap">
<style>
  :root {
    --bg: #bdbdbd;
    --paper: #ffffff;
    --ink: #333333;
    --blue: #1a8fdc;
    --blue-deep: #0d5fbf;
    --card-dark: #242424;
    --card-dark-2: #2e2e2e;
    --edge: #1479d6;
  }
  * { box-sizing: border-box; margin: 0; padding: 0; }
  html, body { width: 1200px; height: 800px; overflow: hidden; }
  body {
    background: linear-gradient(135deg, #a9a9a9 0%, var(--bg) 55%, #cfcfcf 100%);
    position: relative;
    font-family: "Arimo", Arial, sans-serif;
  }
  .card {
    position: absolute;
    top: 250px;
    width: 520px;
    height: 297px;
    border-bottom: 3px solid var(--edge);
    box-shadow: 0 18px 30px rgba(0,0,0,.28);
  }
  .card--front { left: 50px; background: var(--paper); }
  .card--back { left: 630px; background: var(--card-dark); overflow: hidden; }

  .wordmark {
    font-family: "Michroma", "Arial Black", sans-serif;
    color: var(--blue);
    line-height: 1.15;
    letter-spacing: 1px;
    display: flex;
    align-items: center;
    gap: 12px;
  }
  .wordmark__square { width: 16px; height: 16px; background: var(--blue); flex: none; }
  .card--front .wordmark {
    position: absolute; left: 120px; top: 52px; font-size: 26px;
  }
  .divider {
    position: absolute; left: 34px; right: 34px; top: 190px;
    height: 1px; background: var(--blue);
  }
  .person { position: absolute; left: 34px; top: 130px; }
  .person__name {
    font-family: "Michroma", "Arial Black", sans-serif;
    color: var(--blue-deep); font-size: 20px; letter-spacing: 1px;
  }
  .person__title { color: var(--ink); font-size: 15px; margin-top: 4px; }
  .contacts { position: absolute; left: 34px; top: 206px; list-style: none; }
  .contacts li {
    display: flex; align-items: center; gap: 10px;
    font-size: 15px; color: var(--ink); margin-bottom: 6px;
  }
  .contacts svg { width: 16px; height: 16px; fill: var(--blue); flex: none; }

  .pattern {
    position: absolute; inset: 0;
    background: linear-gradient(135deg, var(--card-dark-2) 0%, var(--card-dark) 60%, #1c1c1c 100%);
  }
  .card--back .wordmark {
    position: absolute; right: 40px; top: 120px; font-size: 24px;
  }
</style>
</head>
<body>
  <section class="card card--front">
    <div class="wordmark"><span class="wordmark__square"></span>CORVANE<br>ELECTRIC</div>
    <div class="person">
      <p class="person__name">WREN OSLOBY</p>
      <p class="person__title">Journeyman Electrician</p>
    </div>
    <div class="divider"></div>
    <ul class="contacts">
      <li>
        <svg viewBox="0 0 24 24" aria-hidden="true"><path d="M6.6 10.8a15.1 15.1 0 0 0 6.6 6.6l2.2-2.2a1 1 0 0 1 1-.25 11.4 11.4 0 0 0 3.6.57 1 1 0 0 1 1 1V20a1 1 0 0 1-1 1A17 17 0 0 1 3 4a1 1 0 0 1 1-1h3.5a1 1 0 0 1 1 1c0 1.25.2 2.45.57 3.57a1 1 0 0 1-.25 1z"/></svg>
        1.360.428.6037
      </li>
      <li>
        <svg viewBox="0 0 24 24" aria-hidden="true"><path d="M2 5h20v14H2z M2 5l10 8 10-8" fill="none" stroke="#1a8fdc" stroke-width="2"/><path d="M2 5h20l-10 8z"/></svg>
        KLXCorvaneElectric@mailvex.net
      </li>
    </ul>
  </section>

  <section class="card card--back">
    <div class="pattern" role="img" aria-label="Embossed repeating brand-mark pattern in dark gloss"></div>
    <div class="wordmark"><span class="wordmark__square"></span>CORVANE<br>ELECTRIC</div>
  </section>
</body>
</html>
```